Charity website needing new website design

Hi there. We are looking to get a revamped website for our non for profit charity. We specialise in eye cataract surgeries and ear care around the world. Please visit our website brightpathrelief.org.au for the current layout.
I have attached a brief with photos. The about us page please include an interactive map showing our locations we operate in. The website should be easy to use, match our logo design and be clear to navigate. Pixelvault and other images can be used if they fit the scheme of the website and feel. The donation page should incorporate the gateway to receive donations. The team page should have each photo of the team member next to it. Please compare to other charity websites such as KORAMEN, Globe Harbor etc. Another website which has a lovely and easy to use scheme is tlnqaustralia.org.au
The tabs should be in the following order:
About us, Why Health? Our Team, Eye Care Programs, Ear Care Programs, Contact Us, Donate.
Please make sure the website is both compatible with mobile & computer.
The Registered Charity Logo can be at the footer of the page with details of brightpath etc

```html
<!DOCTYPE html>
<html lang="en">
<head>
<meta charset="utf-8">
<title>Brightpath Aid Foundation</title>
<link href="https://fonts.googleapis.com/css2?family=Plus+Jakarta+Sans:wght@400;500;600;700&display=swap" rel="stylesheet">
<style>
:root{
  --navy:#2b4a63;
  --ink:#1f2a33;
  --muted:#6f7780;
  --orange:#f4ad3d;
  --green:#3cb46e;
  --grey:#f4f4f4;
  --deep:#0b4a67;
  --white:#ffffff;
}
*{box-sizing:border-box;margin:0;padding:0}
html,body{width:1200px;height:3869px;overflow:hidden}
body{position:relative;background:var(--white);font-family:"Plus Jakarta Sans",sans-serif;color:var(--ink)}
.abs{position:absolute}
.photo{position:absolute;border-radius:18px;overflow:hidden}
a{color:inherit;text-decoration:none}

/* header */
.brand{left:84px;top:30px;display:flex;align-items:center;gap:10px}
.brand-dot{width:34px;height:34px;border-radius:50%;background:var(--navy)}
.brand-name{font-weight:700;font-size:19px;color:var(--navy);line-height:1.05}
.nav{right:84px;top:38px;display:flex;gap:40px;font-size:12.5px;color:var(--muted)}
.nav .active{color:var(--ink);font-weight:600;border-bottom:2px solid var(--orange);padding-bottom:6px}

/* hero */
.hero-title{left:84px;top:94px;font-size:56px;font-weight:700;line-height:1.08;color:var(--navy);letter-spacing:-.5px}
.hero-lead{left:608px;top:110px;width:500px;font-size:16px;line-height:1.6;color:var(--ink)}
.btn{display:inline-flex;align-items:center;justify-content:center;background:var(--orange);color:var(--white);font-weight:600;border-radius:22px}
.hero-actions{left:608px;top:180px;display:flex;align-items:center;gap:20px}
.hero-actions .btn{width:132px;height:34px;font-size:12.5px}
.link-under{font-size:12.5px;font-weight:600;border-bottom:1.5px solid currentColor;padding-bottom:2px}
.hero-photo{left:84px;top:254px;width:1032px;height:404px;background:linear-gradient(120deg,#c9a27a,#e0bf98 45%,#b88a62)}
.play{position:absolute;width:54px;height:54px;border-radius:50%;background:var(--green);display:flex;align-items:center;justify-content:center}
.stats{left:84px;top:692px;width:1032px;display:flex;justify-content:space-between;align-items:center}
.stat b{display:block;font-size:24px;font-weight:700;color:var(--navy)}
.stat span{display:block;font-size:16px;color:var(--ink);margin-top:8px}
.dot{width:9px;height:9px;border-radius:50%;background:var(--orange)}

/* about */
.band{left:0;width:1200px;background:var(--grey)}
.about-photo1{left:84px;top:891px;width:475px;height:220px;background:linear-gradient(120deg,#c49c74,#e3c7a3,#b4875f)}
.stat-card{left:84px;top:1128px;width:158px;height:159px;border-radius:18px;background:var(--orange);color:var(--white);padding:56px 14px 0}
.stat-card b{font-size:40px;font-weight:700;display:block;line-height:1}
.stat-card span{font-size:12px;line-height:1.6;display:block;margin-top:4px}
.about-photo2{left:258px;top:1128px;width:301px;height:159px;background:linear-gradient(120deg,#7fa5c7,#d9b23a 55%,#5c7f9d)}
.section-title{font-size:42px;font-weight:700;color:var(--navy);letter-spacing:-.3px}
.about-title{left:608px;top:926px}
.about-text{left:608px;top:984px;width:510px;font-size:16px;line-height:1.57;color:var(--muted)}
.about-link{left:608px;top:1238px;color:var(--orange);font-size:13px;font-weight:600;border-bottom:1.5px solid var(--orange);padding-bottom:2px}

/* donations */
.section-sub{font-size:16px;color:var(--muted)}
.card{position:absolute;top:1547px;width:332px;height:500px;border-radius:16px;padding:14px 12px}
.card.raised{background:var(--white);box-shadow:0 8px 28px rgba(0,0,0,.07)}
.card-photo{width:308px;height:254px;border-radius:14px}
.card h3{font-size:24px;font-weight:600;margin-top:24px;color:var(--ink)}
.card p{font-size:12.5px;line-height:1.6;color:var(--muted);margin-top:10px}
.bar{height:5px;border-radius:3px;background:#eeeeee;margin-top:16px;position:relative}
.bar i{position:absolute;left:0;top:0;height:5px;border-radius:3px;background:var(--orange)}
.card-foot{display:flex;justify-content:space-between;align-items:flex-end;margin-top:18px}
.card-foot small{font-size:12.5px;display:block}
.card-foot b{font-size:21px;font-weight:600;display:block;margin-top:4px}
.card-foot .btn{width:114px;height:46px;border-radius:4px;font-size:12.5px}

/* stories */
.story{position:absolute;top:2355px;width:332px}
.story-photo{height:243px;border-radius:12px}
.story h4{font-size:20px;font-weight:600;line-height:1.35;color:var(--navy);margin-top:22px}
.story-meta{display:flex;justify-content:space-between;align-items:center;margin-top:18px;font-size:12.5px;color:var(--muted)}
.story-meta .author{display:flex;align-items:center;gap:8px;color:var(--navy);font-weight:600}
.avatar{width:20px;height:20px;border-radius:50%;background:#c7b4a6}

/* feature + footer */
.deep{left:0;top:3069px;width:1200px;height:800px;background:var(--deep)}
.feature-card{left:84px;top:2863px;width:1032px;height:577px;background:var(--white);border-radius:20px}
.feature-photo{left:104px;top:2884px;width:992px;height:425px;background:linear-gradient(120deg,#6e4e35,#a68262 50%,#4d6d8e);border-radius:14px}
.notch{left:535px;top:3368px;width:130px;height:130px;border-radius:50%;background:var(--deep)}
.badge{left:550px;top:3383px;width:100px;height:100px;border-radius:50%;background:var(--white);border:5px solid var(--orange)}
.foot-nav{left:0;top:3580px;width:1200px;display:flex;justify-content:center;gap:54px;font-size:12.5px;font-weight:600;color:var(--white)}
.foot-nav .active{color:var(--orange)}
.sub-title{left:0;top:3644px;width:1200px;text-align:center;font-size:24px;font-weight:600;color:var(--white)}
.sub-form{left:306px;top:3695px;display:flex;gap:15px}
.sub-input{width:454px;height:39px;border-radius:20px;background:var(--white);font-size:12.5px;color:var(--muted);padding:12px 20px}
.sub-form .btn{width:119px;height:39px;font-size:12.5px}
.foot-rule{left:84px;top:3808px;width:1032px;height:1px;background:rgba(255,255,255,.2)}
.copy{left:84px;top:3823px;font-size:12.5px;color:rgba(255,255,255,.7)}
.legal{right:84px;top:3823px;font-size:12.5px;color:rgba(255,255,255,.7)}
</style>
</head>
<body>

<header>
  <div class="abs brand"><span class="brand-dot"></span><span class="brand-name">BRIGHTPATH AID<br><span style="font-size:11px;font-weight:600">FOUNDATION</span></span></div>
  <nav class="abs nav">
    <a class="active">Home</a><a>About Us</a><a>Why Health?</a><a>Our Team</a><a>Eye Care Programs</a><a>Contact Us</a>
  </nav>
</header>

<section>
  <h1 class="abs hero-title">Global Basic<br>Healthcare.</h1>
  <p class="abs hero-lead">Through symbiotic health programs brightpath aid foundation provides innovative solutions to Eye and Hearing Health</p>
  <div class="abs hero-actions"><a class="btn">Donate Now</a><a class="link-under">Learn More</a></div>
  <div class="photo hero-photo" role="img" aria-label="Three children holding hands and playing outdoors on sandy ground">
    <span class="play" style="right:14px;bottom:14px"><svg width="14" height="14" viewBox="0 0 14 14"><path d="M4 2l8 5-8 5z" fill="#fff"/></svg></span>
  </div>
  <div class="abs stats">
    <div class="stat"><b>$1M+</b><span>Fund Raised</span></div><span class="dot"></span>
    <div class="stat"><b>500+</b><span>Dedicated Volunteers</span></div><span class="dot"></span>
    <div class="stat"><b>100%</b><span>Delivered Donations</span></div><span class="dot"></span>
    <div class="stat"><b>250K</b><span>Charity Participation</span></div>
  </div>
</section>

<section>
  <div class="abs band" style="top:837px;height:503px"></div>
  <div class="photo about-photo1" role="img" aria-label="Children playing together outdoors"></div>
  <div class="abs stat-card"><b>50%</b><span>of kids worldwide don’t have education</span></div>
  <div class="photo about-photo2" role="img" aria-label="Smiling girl with a young man behind her"></div>
  <h2 class="abs section-title about-title">About Us</h2>
  <p class="abs about-text">Brightpath Aid Foundation is dedicated to improving and transforming the lives of people through enhanced vision and hearing health in the developing world. Our mission is to bridge the gap in access to essential eye and hearing care, ensuring that everyone, regardless of their circumstances, has the opportunity to see and hear clearly. With over 70 years of humanitarian aid across our members, we are passionate to provide innovative, sustainable, ethical and professional symbiotic solutions across multiple health programs.</p>
  <a class="abs about-link">Learn More</a>
</section>

<section>
  <h2 class="abs section-title" style="left:84px;top:1420px">Ongoing Donation</h2>
  <p class="abs section-sub" style="left:84px;top:1485px">Lorem ipsum dolor sit amet, consectetur adipiscing elit.</p>

  <article class="card raised" style="left:84px">
    <div class="card-photo" role="img" aria-label="Eye examination of an elderly man" style="background:linear-gradient(120deg,#8d8d8d,#d9d9d9,#6f6f6f)"></div>
    <h3>Eye Care</h3>
    <p>Curabitur pellentesque elit sit amet leo tincidunt, in bibendum eros rhoncus. Cras pharetra rhoncus purus ut cursus. Duis pharetra dapibus placerat.</p>
    <div class="bar"><i style="width:41%"></i></div>
    <div class="card-foot"><div><small>Reached</small><b>$32,000</b></div><a class="btn">Donate</a></div>
  </article>
  <article class="card" style="left:434px">
    <div class="card-photo" role="img" aria-label="Man receiving an ear check" style="background:linear-gradient(120deg,#5a3a26,#b07e58,#3d2a1d)"></div>
    <h3>Ear Care</h3>
    <p>Curabitur pellentesque elit sit amet leo tincidunt, in bibendum eros rhoncus. Cras pharetra rhoncus purus ut cursus. Duis pharetra dapibus placerat.</p>
    <div class="bar"><i style="width:58%"></i></div>
    <div class="card-foot"><div><small>Reached</small><b>$51,000</b></div><a class="btn">Donate</a></div>
  </article>
  <article class="card" style="left:784px">
    <div class="card-photo" role="img" aria-label="Health worker giving a vaccination" style="background:linear-gradient(120deg,#2f6fb8,#8a6a54,#3a2c24)"></div>
    <h3>General Health</h3>
    <p>Curabitur pellentesque elit sit amet leo tincidunt, in bibendum eros rhoncus. Cras pharetra rhoncus purus ut cursus. Duis pharetra dapibus placerat.</p>
    <div class="bar"><i style="width:23%"></i></div>
    <div class="card-foot"><div><small>Reached</small><b>$24,000</b></div><a class="btn">Donate</a></div>
  </article>
</section>

<section>
  <div class="abs band" style="top:2179px;height:600px"></div>
  <h2 class="abs section-title" style="left:84px;top:2230px">Building a Brighter Future</h2>
  <p class="abs section-sub" style="left:84px;top:2292px">Lorem ipsum dolor sit amet, consectetur adipiscing elit.</p>
  <a class="abs about-link" style="left:1004px;top:2296px;font-size:12.5px">See All Issues</a>

  <article class="story" style="left:84px">
    <div class="story-photo" role="img" aria-label="Community gathered around a new water pump" style="background:linear-gradient(120deg,#d8d3c8,#e8c55a,#9a8f7f)"></div>
    <h4>Nullam at tellus maximus, feugiat turpis ac</h4>
    <div class="story-meta"><span class="author"><span class="avatar"></span>Mara Ellison</span><span>December 24, 2023</span></div>
  </article>
  <article class="story" style="left:434px">
    <div class="story-photo" role="img" aria-label="Clinic worker treating a patient" style="background:linear-gradient(120deg,#3c3a38,#b9ada0,#5b4a3c)"></div>
    <h4>Nullam at tellus maximus, feugiat turpis ac</h4>
    <div class="story-meta"><span class="author"><span class="avatar"></span>Tobin Reyes</span><span>August 30, 2023</span></div>
  </article>
  <article class="story" style="left:784px">
    <div class="story-photo" role="img" aria-label="People standing by a water tap on a tiled base" style="background:linear-gradient(120deg,#b34a4a,#cfcac2,#8a7a5d)"></div>
    <h4>Nullam at tellus maximus, feugiat turpis ac</h4>
    <div class="story-meta"><span class="author"><span class="avatar"></span>Clara Vance</span><span>April 16, 2023</span></div>
  </article>
</section>

<footer>
  <div class="abs deep"></div>
  <div class="abs feature-card"></div>
  <div class="photo feature-photo" role="img" aria-label="Two boys hugging in a school courtyard">
    <span class="play" style="right:14px;bottom:44px"><svg width="14" height="14" viewBox="0 0 14 14"><path d="M4 2l8 5-8 5z" fill="#fff"/></svg></span>
  </div>
  <div class="abs notch"></div>
  <div class="abs badge" role="img" aria-label="Registered charity badge"></div>

  <nav class="abs foot-nav"><a>About Us</a><a class="active">Why Health?</a><a>Our Team</a><a>Contact Us</a></nav>
  <h2 class="abs sub-title">Subscribe to Newsletter</h2>
  <form class="abs sub-form"><div class="sub-input">Enter your email address ...</div><a class="btn">Subscribe</a></form>
  <div class="abs foot-rule"></div>
  <p class="abs copy">Copyright © Brightpath Aid 2024. All rights reserved.</p>
  <p class="abs legal">Privacy Policy &nbsp;|&nbsp; Terms &amp; Condition</p>
</footer>

</body>
</html>
```